Business Cards that are elegant and wow

I want to create and print business cards that represent my brand and stand out from the rest. We want to ensure they stay in our branding and the integrity is not lost. I am happy to look at different shapes like square etc.

It will be printed on very thick cards and will be stylish .

I want to create and print business cards that represent my brand and stand out from the rest. We want to ensure they stay in ur branding and the integrity is not lost. I am happy to look at different shapes like square etc.

Target Market(s)

real estate professionals

Industry/Entity Type

Real Estate

Contact Information for Business Card

Maren Holt
hello@brightfernrealty.com.au
brightfernrealty.com.au
0487 316 252 (SMS)

Colors

Designer to choose colors to be used in the design.

Requirements
Must have
• My logo
• email
• website
• Name
Nice to have
• I like the idea of printing with foil or spot gloss. You want it to stand out in a sea.
Should not have
• I would like you to stay in my colour themes. Don't change the colour of my logo

```html
<!DOCTYPE html>
<html lang="en">
<head>
<meta charset="utf-8">
<title>Bright Fern Realty – Business Card</title>
<link href="https://fonts.googleapis.com/css2?family=Crimson+Pro:ital,wght@0,400;0,600;0,700;1,400&display=swap" rel="stylesheet">
<style>
  :root {
    --page: #ffffff;
    --navy: #0a0050;
    --white: #ffffff;
    --pink: #ee0a8c;
    --pink-deep: #9c1062;
    --sky-blue: #2aa3f0;
    --silver-light: #d9d9dc;
    --silver-mid: #a9a9ad;
    --silver-dark: #8e8e93;
  }
  html, body {
    margin: 0;
    padding: 0;
    width: 1200px;
    height: 1200px;
    overflow: hidden;
    background: var(--page);
  }
  .canvas {
    position: relative;
    width: 1200px;
    height: 1200px;
    font-family: "Crimson Pro", Georgia, serif;
  }
  .card {
    position: absolute;
    top: 339px;
    width: 325px;
    height: 502px;
    background: var(--navy);
    overflow: hidden;
  }
  .card--front { left: 207px; }
  .card--back { left: 649px; }

  .foil-disc {
    position: absolute;
    top: 80px;
    width: 90px;
    height: 90px;
    border-radius: 50%;
    background: linear-gradient(90deg, var(--silver-dark) 0%, var(--silver-light) 45%, var(--silver-mid) 75%, var(--silver-light) 100%);
  }
  .card--front .foil-disc { left: 38px; }
  .card--back .foil-disc { left: 38px; }

  .contact {
    position: absolute;
    left: 137px;
    top: 60px;
    color: var(--white);
  }
  .contact__brand {
    margin: 0;
    font-size: 22px;
    font-weight: 600;
    letter-spacing: 0.2px;
    line-height: 1;
  }
  .contact__tagline {
    margin: 2px 0 0;
    font-size: 11.5px;
    font-style: italic;
    line-height: 1.2;
  }
  .contact__name {
    margin: 10px 0 6px;
    font-size: 17px;
    font-weight: 700;
    line-height: 1.1;
  }
  .contact__line {
    margin: 0;
    font-size: 11.5px;
    font-style: italic;
    line-height: 20.5px;
  }

  .skyline {
    position: absolute;
    left: 0;
    bottom: 0;
    width: 325px;
    height: 160px;
    background: linear-gradient(180deg, var(--pink) 0%, var(--pink) 45%, var(--pink-deep) 100%);
  }

  .brand-lockup {
    position: absolute;
    left: 0;
    right: 0;
    top: 410px;
    text-align: center;
    color: var(--sky-blue);
  }
  .brand-lockup__row {
    display: flex;
    justify-content: center;
    align-items: center;
    gap: 7px;
  }
  .brand-lockup__dot {
    width: 26px;
    height: 26px;
    border-radius: 50%;
    background: var(--sky-blue);
  }
  .brand-lockup__name {
    font-size: 21px;
    font-weight: 600;
    letter-spacing: 0.5px;
    line-height: 1;
  }
  .brand-lockup__tagline {
    margin: 9px 0 0;
    font-size: 16.5px;
    line-height: 1;
  }
</style>
</head>
<body>
<main class="canvas">
  <section class="card card--front">
    <div class="foil-disc"></div>
    <div class="contact">
      <h1 class="contact__brand">BRIGHT FERN</h1>
      <p class="contact__tagline">real estate professionals</p>
      <h2 class="contact__name">Maren Holt</h2>
      <p class="contact__line">hello@brightfernrealty.com.au</p>
      <p class="contact__line">brightfernrealty.com.au</p>
      <p class="contact__line">0487 316 252 (SMS)</p>
    </div>
    <div class="skyline" role="img" aria-label="Pink city skyline illustration of tall buildings and a spire"></div>
  </section>

  <section class="card card--back">
    <div class="foil-disc"></div>
    <div class="brand-lockup">
      <div class="brand-lockup__row">
        <span class="brand-lockup__dot"></span>
        <span class="brand-lockup__name">BRIGHT FERN REALTY</span>
      </div>
      <p class="brand-lockup__tagline">real estate professionals</p>
    </div>
  </section>
</main>
</body>
</html>
```